Birchfield Dental Care Stationery

create stationery, business cards and envelops for business. Use current logo on website but open to new fonts for the business name. Business name is Birchfield Dental Care, would like below the name added "Cosmetic - Family - Implants" Website is www.birchfielddentalcareQX.example. I would like to have modern look, clean, and professional. The water mark of the logo is a great thing to ad as well.

Target Market(s)

General public, Families, Cosmetic, Implant

Industry/Entity Type

Dental

Font styles to use
Sans Serif

Colors
9bcb3c
000000
757575
c9c9c9

Requirements
Must have
• Would like to see different versions of the current logo. Improvements, color, sytle, and class.
Nice to have
• current font has double "oo" in the Birchfield logo, does not need to have with new logo.

```html
<!DOCTYPE html>
<html lang="en">
<head>
<meta charset="utf-8">
<title>Birchfield Dental Care — Business Cards</title>
<link rel="stylesheet" href="https://fonts.googleapis.com/css2?family=Montserrat:wght@300;400;600&display=swap">
<style>
  :root {
    --bg: #e4e6e4;
    --lime-light: #e2ef8c;
    --lime: #b7d646;
    --lime-deep: #9bcb3c;
    --teal-light: #2aa3a0;
    --teal: #137f7e;
    --teal-dark: #0b5f61;
    --ink: #2e3327;
    --cream: #f3f6dd;
    --accent: #d6e84e;
  }
  * { box-sizing: border-box; margin: 0; padding: 0; }
  html, body { width: 1200px; height: 902px; overflow: hidden; }
  body {
    background: var(--bg);
    font-family: "Montserrat", sans-serif;
    position: relative;
  }

  /* Front card (portrait) */
  .card-front {
    position: absolute;
    left: 150px; top: 151px;
    width: 360px; height: 600px;
    border-radius: 4px;
    overflow: hidden;
    background: radial-gradient(ellipse at 55% 30%, var(--lime-light) 0%, var(--lime) 65%, var(--lime-deep) 100%);
    box-shadow: 0 10px 24px rgba(0,0,0,.18);
  }
  .card-front .waves { position: absolute; left: 0; top: 0; width: 360px; height: 600px; }
  .brand {
    position: absolute;
    top: 118px; left: 0; right: 0;
    text-align: center;
    color: var(--ink);
  }
  .brand-dot {
    display: block;
    width: 54px; height: 54px;
    margin: 0 auto 16px;
    border: 3px solid var(--ink);
    border-radius: 50%;
  }
  .brand-name {
    font-weight: 300;
    color: var(--ink);
  }
  .brand-name .line-1 {
    display: block;
    font-size: 32px;
    letter-spacing: 2px;
    text-transform: uppercase;
    line-height: 1.1;
  }
  .brand-name .line-2 {
    display: block;
    font-size: 27px;
    letter-spacing: 3px;
    line-height: 1.15;
  }
  .tagline {
    margin-top: 12px;
    font-size: 11px;
    font-weight: 400;
    letter-spacing: 2px;
    text-transform: uppercase;
    color: var(--ink);
  }
  .holder {
    position: absolute;
    left: 0; right: 0; top: 424px;
    text-align: center;
    color: var(--accent);
  }
  .holder-name { font-size: 19px; font-weight: 600; letter-spacing: 1.5px; text-transform: uppercase; }
  .holder-role { font-size: 12px; letter-spacing: 2px; margin-top: 5px; text-transform: uppercase; }
  .web {
    position: absolute;
    left: 0; right: 0; top: 530px;
    text-align: center;
    color: var(--accent);
    font-size: 12px;
    letter-spacing: .5px;
    text-transform: uppercase;
  }

  /* Back card (landscape) */
  .card-back {
    position: absolute;
    left: 560px; top: 271px;
    width: 600px; height: 360px;
    border-radius: 4px;
    overflow: hidden;
    background: radial-gradient(ellipse at 60% 25%, var(--teal-light) 0%, var(--teal) 55%, var(--teal-dark) 100%);
    box-shadow: 0 10px 24px rgba(0,0,0,.18);
  }
  .watermark {
    position: absolute;
    left: -60px; top: 150px;
    width: 280px; height: 280px;
    border-radius: 50%;
    border: 14px solid rgba(8,60,62,.35);
  }
  .contact {
    position: absolute;
    left: 180px; right: 24px; top: 48px;
    display: flex; flex-direction: column; align-items: center;
    color: var(--cream);
    text-align: center;
    text-transform: uppercase;
  }
  .contact-line { font-size: 14px; letter-spacing: .5px; line-height: 1.45; }
  .contact-line.email { font-size: 12px; letter-spacing: 0; }
  .divider {
    display: flex; align-items: center; gap: 10px;
    margin: 16px 0;
  }
  .divider .rule { width: 120px; height: 2px; background: var(--accent); }
  .divider svg { width: 16px; height: 16px; }
</style>
</head>
<body>

<section class="card-front" aria-label="Business card front">
  <svg class="waves" viewBox="0 0 360 600" aria-hidden="true">
    <defs>
      <linearGradient id="bandFill" x1="0" y1="0" x2="0" y2="1">
        <stop offset="0" stop-color="#1c9a98"/>
        <stop offset="1" stop-color="#0f7574"/>
      </linearGradient>
    </defs>
    <path d="M0 352 C110 368 230 395 360 440 L360 600 L0 600 Z" fill="url(#bandFill)"/>
    <path d="M0 346 C110 362 230 389 360 434" fill="none" stroke="#2fb2b0" stroke-width="3"/>
    <path d="M0 452 C120 468 250 500 360 545" fill="none" stroke="#d6e84e" stroke-width="3"/>
  </svg>

  <div class="brand">
    <span class="brand-dot"></span>
    <div class="brand-name">
      <span class="line-1">Birchfield</span>
      <span class="line-2">dental care</span>
    </div>
    <div class="tagline">Cosmetic - Family - Implants</div>
  </div>

  <div class="holder">
    <div class="holder-name">Name Surname</div>
    <div class="holder-role">Psicoterapeuta</div>
  </div>
  <div class="web">birchfielddentalcareqx.example</div>
</section>

<section class="card-back" aria-label="Business card back">
  <div class="watermark" role="img" aria-label="Faint practice mark watermark"></div>

  <div class="contact">
    <div class="divider">
      <span class="rule"></span>
      <svg viewBox="0 0 16 16" aria-hidden="true"><path d="M8 1a5 5 0 0 0-5 5c0 4 5 9 5 9s5-5 5-9a5 5 0 0 0-5-5zm0 7a2 2 0 1 1 0-4 2 2 0 0 1 0 4z" fill="#d6e84e"/></svg>
      <span class="rule"></span>
    </div>
    <div class="contact-line">1250 S Birchfield Rd</div>
    <div class="contact-line">Maple Hollow, QX 40123-0000</div>

    <div class="divider">
      <span class="rule"></span>
      <svg viewBox="0 0 16 16" aria-hidden="true"><rect x="3" y="1.5" width="10" height="13" rx="2" fill="none" stroke="#d6e84e" stroke-width="1.6"/><rect x="6" y="11.5" width="4" height="1.2" fill="#d6e84e"/></svg>
      <span class="rule"></span>
    </div>
    <div class="contact-line">555-014-2290</div>

    <div class="divider">
      <span class="rule"></span>
      <svg viewBox="0 0 16 16" aria-hidden="true"><rect x="1.5" y="3.5" width="13" height="9" fill="none" stroke="#d6e84e" stroke-width="1.6"/><path d="M1.5 3.5 L8 9 L14.5 3.5" fill="none" stroke="#d6e84e" stroke-width="1.6"/></svg>
      <span class="rule"></span>
    </div>
    <div class="contact-line email">n.surname@birchfielddentalcareqx.example</div>
  </div>
</section>

</body>
</html>
```